Letterhead That Inspires Trust

Birchwell Deed Services, LLC, (BDS) fixes technical problems with property deeds. The problems usually surface when someone tries to buy, sell or mortgage a piece of real estate and one of the lawyers involved find a title defect (a lien, an undischarged mortgage, a deceased person still on the title, unpaid taxes, etc.). BDS then gets involved and often has to contact prior property owners to get them to sign paperwork fixing the problem. We need a letterhead that will a) convey the seriousness of what we are trying to do, b) cause the recipients of our letters to recognize the importance of what are trying to do, and c) convey that we are a established and trustworthy company. We want it to include an image that suggests we are a problem solving company. Attached is an image we think might work; you can use it or not. In addition to our name (Birchwell Deed Services, LLC), the letterhead must include our address and phone number: 418 Calder Avenue, Suite 207, Providence, RI 02917 (401) 555-0372. We are thinking something straightforward without unnecessary colors or graphics.

```html
<!DOCTYPE html>
<html lang="en">
<head>
<meta charset="utf-8">
<title>Birchwell Deed Services, LLC — Letterhead</title>
<link href="https://fonts.googleapis.com/css2?family=Cinzel:wght@700&family=Barlow:wght@400&family=Outfit:wght@400&display=swap" rel="stylesheet">
<style>
  :root {
    --backdrop: #e4e4e4;
    --paper: #ffffff;
    --band: #5e5e5e;
    --title: #555555;
    --ink: #404040;
    --rule: #2e2e2e;
    --photo-wood: #efe3d2;
    --photo-green: #d6ecc4;
    --sig-ink: #d9d9d9;
  }
  * { box-sizing: border-box; margin: 0; padding: 0; }
  html, body {
    width: 1200px; height: 1200px; overflow: hidden;
    background: var(--backdrop);
  }
  .letterhead {
    position: absolute; left: 197px; top: 30px;
    width: 805px; height: 1140px;
    background: var(--paper);
  }
  .top-band {
    position: absolute; left: 0; top: 0; width: 100%; height: 20px;
    background: var(--band);
  }
  .company-name {
    position: absolute; top: 60px; left: 0; width: 100%;
    text-align: center;
    font-family: "Cinzel", "Trajan Pro", serif;
    font-weight: 700; font-size: 44px; line-height: 42px;
    color: var(--title);
  }
  .recipient, .salutation, .body-copy, .closing {
    position: absolute; left: 76px;
    font-family: "Barlow", "DIN", sans-serif;
    font-size: 15px; color: var(--ink); letter-spacing: 0.2px;
  }
  .recipient { top: 260px; line-height: 19.6px; }
  .salutation { top: 394px; }
  .problem-image {
    position: absolute; left: 177px; top: 462px; width: 462px; height: 231px;
    background: radial-gradient(ellipse at 55% 45%, var(--photo-green) 0%, var(--photo-wood) 40%, rgba(255,255,255,0) 72%);
    opacity: 0.7;
  }
  .body-copy { top: 440px; width: 660px; line-height: 24.4px; }
  .signature {
    position: absolute; left: 72px; top: 864px; width: 141px; height: 71px;
    background: linear-gradient(90deg, rgba(255,255,255,0), var(--sig-ink) 50%, rgba(255,255,255,0));
    opacity: 0.5;
  }
  .closing { top: 940px; }
  .footer-rule {
    position: absolute; left: 77px; top: 1088px; width: 637px; height: 1.5px;
    background: var(--rule);
  }
  .footer-contact {
    position: absolute; left: 0; top: 1097px; width: 100%;
    text-align: center;
    font-family: "Outfit", sans-serif; font-size: 13px; color: var(--ink);
  }
  .footer-contact svg { vertical-align: -2px; margin: 0 2px 0 4px; }
</style>
</head>
<body>
  <main class="letterhead">
    <div class="top-band"></div>
    <h1 class="company-name">Birchwell Deed<br>Services, LLC</h1>

    <address class="recipient" style="font-style:normal">
      Mr. Martin Hale<br>President<br>Ledgerline Accountants<br>111 Street Name,<br>City State, 12345
    </address>

    <p class="salutation">Dear :</p>

    <div class="problem-image" role="img" aria-label="Faint photo of wooden figures linked by green lines around one green figure, suggesting problem solving"></div>

    <div class="body-copy">
      <p>Lorem ipsum dolor sit amet, consectetur adipiscing elit. Aenean ut ipsum eget massa hendrerit vestibulum vel in velit. Donec pretium neque velit.</p>
      <p>Aliquam porta lectus nec mauris ornare venenatis. Vivamus non est turpis, et cursus sem. Mauris vehicula erat in diam auctor at bibendum nisl lacinia.</p>
      <p>Morbi imperdiet neque vehicula nunc convallis gravida. Vestibulum iaculis pretium placerat. Integer consequat, est sit amet facilisis eleifend, nibh nibh varius orci, eget dapibus arcu dui non purus. Pellentesque in magna mauris. Duis enim sapien, dictum vitae condimentum a, pulvinar vel lacus. Mauris et molestie nibh. Vestibulum vitae nulla at metus elementum porta sit amet interdum elit. Nulla sollicitudin neque eu nulla volutpat congue.</p>
      <p>Etiam pellentesque, velit id dapibus fermentum, turpis sapien ornare dui, ac tincidunt ligula odio congue purus. Nunc sed ante dui, in porta lectus. Cras nec sem lorem. In hac habitasse platea dictumst. Maecenas id diam quis dui porta tristique. Sed id egestas felis. Donec ullamcorper mattis posuere. Phasellus fermentum eleifend tortor vel dapibus. Vestibulum ante ipsum.</p>
    </div>

    <div class="signature" role="img" aria-label="Handwritten signature"></div>
    <p class="closing">Sincerely,</p>

    <div class="footer-rule"></div>
    <p class="footer-contact">418 Calder Avenue, Suite 207,&nbsp; Providence, RI 02917 |<svg width="12" height="12" viewBox="0 0 24 24" aria-hidden="true"><path fill="#404040" d="M6.6 10.8a15.1 15.1 0 0 0 6.6 6.6l2.2-2.2a1 1 0 0 1 1-.25 11.4 11.4 0 0 0 3.6.57 1 1 0 0 1 1 1V20a1 1 0 0 1-1 1A17 17 0 0 1 3 4a1 1 0 0 1 1-1h3.5a1 1 0 0 1 1 1c0 1.25.2 2.45.57 3.57a1 1 0 0 1-.25 1z"/></svg>(401) 555-0372</p>
  </main>
</body>
</html>
```